Square Business Cards for Our Restaurant / Event Venue

We need square business cards designed for the management team of our event venue and restaurant. On one side of the card should be the the Harbor Lantern 7 logo and URL www.harborlantern7.example. On the other side should be the Ember Logo and URL www.emberhall7.example. All employee details should be on the side with Ember logo. There will be a total of 5 cards to be created with the design.

Clara Bennquist
clara@harborlantern7.example

main 555.418.3072
direct 555.730.2946

4831 West Orchard Lane SE
Washington, DC 90417

Industry/Entity Type

Business

```html
<!DOCTYPE html>
<html lang="en">
<head>
<meta charset="utf-8">
<title>Harbor Lantern 7 — Square Business Cards</title>
<link href="https://fonts.googleapis.com/css2?family=Open+Sans:wght@400;600;700&display=swap" rel="stylesheet">
<style>
  :root {
    --stage: #2e2e30;
    --card-dark: #1c1a1d;
    --card-mid: #2a272b;
    --brand-red: #c0121f;
    --brand-red-deep: #a40d18;
    --text-light: #d9d9d9;
    --text-white: #ffffff;
    --logo-grey: #c8c8c8;
  }
  * { margin: 0; padding: 0; box-sizing: border-box; }
  html, body {
    width: 1200px; height: 900px; overflow: hidden;
    background: var(--stage);
    font-family: "Open Sans", Arial, sans-serif;
  }
  .sheet {
    position: relative; width: 1200px; height: 900px;
    display: flex; align-items: center; justify-content: center; gap: 80px;
  }
  .card {
    position: relative; width: 480px; height: 480px;
    border-radius: 30px; overflow: hidden;
    background: var(--card-dark);
    box-shadow: 0 12px 30px rgba(0,0,0,.45);
  }
  .card__backdrop {
    position: absolute; inset: 0;
    background: linear-gradient(160deg, #333035 0%, #1f1d21 55%, #18161a 100%);
  }
  .card__band {
    position: absolute; left: 0; right: 0; bottom: 34px; height: 66px;
    background: var(--brand-red);
    display: flex; align-items: flex-end; justify-content: center;
    padding-bottom: 12px;
    border-top: 16px solid var(--brand-red-deep);
  }
  .card__url {
    color: var(--text-white); font-weight: 600; font-size: 17px; letter-spacing: .2px;
  }

  /* Front */
  .front__emblem {
    position: absolute; left: 50%; top: 44%;
    width: 250px; height: 250px; border-radius: 50%;
    transform: translate(-50%, -50%);
    background: var(--brand-red);
    display: flex; align-items: center; justify-content: center; text-align: center;
  }
  .front__name {
    color: var(--card-dark); font-weight: 600; font-size: 34px; line-height: 1.15;
  }

  /* Back */
  .back { background: var(--card-dark); }
  .back__details {
    position: absolute; top: 30px; left: 0; right: 0; text-align: center;
  }
  .back__person {
    color: var(--text-light); font-weight: 700; font-size: 21px; text-transform: uppercase; letter-spacing: .5px;
  }
  .back__email {
    color: var(--brand-red); font-weight: 600; font-size: 15px; margin-top: 2px;
  }
  .back__phones {
    display: flex; justify-content: center; gap: 22px; margin-top: 8px;
    color: var(--text-light); font-size: 16px; font-weight: 600;
  }
  .phone { display: flex; align-items: center; gap: 7px; }
  .phone svg { width: 16px; height: 16px; }
  .back__logo {
    position: absolute; top: 150px; left: 0; right: 0; text-align: center;
    color: var(--logo-grey); font-weight: 700; font-size: 84px; line-height: 1;
  }
  .back__address {
    position: absolute; top: 272px; left: 0; right: 0; text-align: center;
    color: var(--text-light); font-weight: 600; font-size: 16px; line-height: 1.45;
  }
</style>
</head>
<body>
<main class="sheet">

  <section class="card front" aria-label="Card front">
    <div class="card__backdrop" role="img" aria-label="Dim photograph of the venue building facade"></div>
    <div class="front__emblem">
      <span class="front__name">Harbor<br>Lantern 7</span>
    </div>
    <div class="card__band"><span class="card__url">www.harborlantern7.example</span></div>
  </section>

  <section class="card back" aria-label="Card back">
    <div class="back__details">
      <div class="back__person">Clara Bennquist</div>
      <div class="back__email">clara@harborlantern7.example</div>
      <div class="back__phones">
        <span class="phone">
          <svg viewBox="0 0 16 16" aria-hidden="true">
            <rect x="1" y="1" width="14" height="14" rx="4" fill="none" stroke="var(--brand-red)" stroke-width="1.6"/>
            <path d="M5.5 4.5c-.6 0-1 .5-1 1 .2 3.2 2.8 5.8 6 6 .5 0 1-.4 1-1v-1l-1.8-.7-.8.8c-1-.5-1.8-1.3-2.3-2.3l.8-.8L6.7 4.5z" fill="var(--brand-red)"/>
          </svg>555.418.3072
        </span>
        <span class="phone">
          <svg viewBox="0 0 16 16" aria-hidden="true">
            <rect x="1" y="1" width="14" height="14" rx="4" fill="none" stroke="var(--brand-red)" stroke-width="1.6"/>
            <path d="M5.5 4.5c-.6 0-1 .5-1 1 .2 3.2 2.8 5.8 6 6 .5 0 1-.4 1-1v-1l-1.8-.7-.8.8c-1-.5-1.8-1.3-2.3-2.3l.8-.8L6.7 4.5z" fill="var(--brand-red)"/>
          </svg>555.730.2946
        </span>
      </div>
    </div>
    <div class="back__logo">Ember</div>
    <div class="back__address">4831 West Orchard Lane SE<br>Washington, DC 90417</div>
    <div class="card__band"><span class="card__url">www.emberhall7.example</span></div>
  </section>

</main>
</body>
</html>
```